Wedding Expo Flyer Design

Flyer : 216mm x 139mm
We are looking to design a double sided flyer to hand out at a wedding expo we are advertising at. These fliers need to look professional and elegant, and make good use of the space on the flyer, without looking cluttered.

On one side will be advertising a deal we are offering and a voucher code to enter on our website, “Now here’s something to smile about!” “Exclusive to The Vow and Veil Showcase! Book now and pay only $199 for our most popular treatment (normal price $599). Bring your partner or a friend and pay only $150 each!” Flier should include a photo of a smiling bride and groom.

On the other side of the flier we would like to tell our customers who we are, and what we do and include our logo and a design/photo.

“Pearlcrest Dental is a speciality teeth whitening clinic run by qualified practitioners. We use a revolutionary low sensitivity whitening gel meaning our treatments are fast, painless and results are guaranteed! For more information and to read some our patient testimonials please visit our website - www.pearlcrestdental.co.nz”

Located 48 Marlow Avenue, Henderson or we offer a mobile service.

Fully qualified practitioners, KDOGRB (Kiwi Dental Oral Glow Registry Board) registered (include small logo)

Our phone number is 0800 GLOWUP

Target Market(s)

Male and female aged 20-39 attending a wedding/wedding expo

Industry/Entity Type

Advertising

Requirements
Must have
• Must include our logo and KDOGRB logo on the informative side of the flyer.
Nice to have
• Bride and groom on deal side of flyer. European bride & Groom.

```html
<!DOCTYPE html>
<html lang="en">
<head>
<meta charset="utf-8">
<title>Pearlcrest Dental – Showcase Offer Flyer</title>
<link href="https://fonts.googleapis.com/css2?family=Roboto+Condensed:wght@400;700&display=swap" rel="stylesheet">
<style>
  :root {
    --navy: #16264a;
    --ink: #1c2b4d;
    --paper: #ffffff;
    --voucher-field: #c9cbd0;
    --rule: #9aa0ad;
  }
  * { margin: 0; padding: 0; box-sizing: border-box; }
  html, body { width: 773px; height: 1200px; overflow: hidden; background: var(--paper); }
  .flyer {
    position: relative;
    width: 773px;
    height: 1200px;
    background: var(--paper);
    font-family: "Roboto Condensed", "Arial Narrow", sans-serif;
    color: var(--ink);
    overflow: hidden;
  }
  .hero-photo {
    position: absolute;
    left: 0; top: 0;
    width: 773px; height: 640px;
    background:
      linear-gradient(180deg, rgba(255,255,255,0) 70%, #ffffff 100%),
      radial-gradient(ellipse at 62% 30%, #f3e2d4 0%, #e2c9b6 22%, rgba(226,201,182,0) 48%),
      radial-gradient(ellipse at 18% 45%, #3b3f4a 0%, #5a5e68 28%, rgba(90,94,104,0) 55%),
      linear-gradient(160deg, #d9d6d2 0%, #ecebea 45%, #f6f6f6 100%);
  }
  .brand {
    position: absolute;
    top: 26px; right: 28px;
    display: flex; align-items: center; gap: 8px;
    font-weight: 700;
    font-size: 26px;
    color: var(--navy);
  }
  .brand-dot {
    width: 14px; height: 14px;
    border-radius: 50%;
    background: var(--navy);
  }
  .offer {
    position: absolute;
    left: 0; right: 0; top: 648px;
    text-align: center;
  }
  .offer-intro {
    font-size: 38px;
    font-weight: 400;
    line-height: 1;
  }
  .offer-title {
    font-size: 118px;
    font-weight: 700;
    line-height: 1;
    margin-top: 14px;
    letter-spacing: 1px;
    color: var(--navy);
  }
  .offer-event {
    font-size: 42px;
    font-weight: 400;
    line-height: 1;
    margin-top: 6px;
  }
  .offer-price {
    font-size: 50px;
    font-weight: 700;
    line-height: 1;
    margin-top: 10px;
    color: var(--navy);
  }
  .offer-detail {
    font-size: 27px;
    line-height: 1.15;
    margin-top: 12px;
  }
  .offer-detail strong { font-weight: 700; }
  .side-rule {
    position: absolute;
    top: 735px;
    width: 2px; height: 90px;
    background: var(--rule);
  }
  .side-rule.left { left: 62px; }
  .side-rule.right { right: 62px; }
  .voucher-band {
    position: absolute;
    left: 0; bottom: 0;
    width: 773px; height: 88px;
    background: var(--navy);
    display: flex; align-items: center; justify-content: center;
    gap: 22px;
  }
  .voucher-label {
    color: var(--paper);
    font-size: 22px;
    font-weight: 700;
  }
  .voucher-field {
    width: 172px; height: 36px;
    background: var(--voucher-field);
  }
</style>
</head>
<body>
  <main class="flyer">
    <div class="hero-photo" role="img" aria-label="Photo of a smiling bride in pearls being kissed on the cheek by her groom in a suit"></div>

    <div class="brand"><span class="brand-dot"></span>Pearlcrest Dental</div>

    <span class="side-rule left"></span>
    <span class="side-rule right"></span>

    <section class="offer">
      <p class="offer-intro">Now here’s something to smile about!</p>
      <h1 class="offer-title">EXCLUSIVE</h1>
      <p class="offer-event">To The Vow and Veil Showcase!</p>
      <p class="offer-price">Book now &amp; pay only $199!</p>
      <p class="offer-detail">For our most popular treatment (normal price $599)<br>
        <strong>Bring</strong> your <strong>partner</strong> or a friend and <strong>pay</strong><br>
        <strong>only $150 each!*</strong></p>
    </section>

    <footer class="voucher-band">
      <span class="voucher-label">Voucher Code:</span>
      <span class="voucher-field"></span>
    </footer>
  </main>
</body>
</html>
```